KBMR new business card design

We need a business card design for our established business which is Australia wide however based in Melbourne. We are a young team of Financial Planners who specialize in Insurance and Basic super advice for people like us.

We are people who help our clients get things done in a timely and cost effective manner whilst having a good time and a laugh along the way.

We would like this to have a consistent feel with our new e-brochure which i have attached from a color and font perspective.

Industry/Entity Type

Business

Requirements
Must have
• We do not need specific address details rather just the states we are in:

VIC/NSW/QLD/TAS
Nice to have
• Curved edge to mate the brochure

```html
<!DOCTYPE html>
<html lang="en">
<head>
<meta charset="utf-8">
<title>KBMR Planning – Business Card</title>
<link rel="stylesheet" href="https://fonts.googleapis.com/css2?family=Arimo:wght@400;700&display=swap">
<style>
  :root {
    --bg: #dcdcdc;
    --card: #2f2f30;
    --green: #5cc43a;
    --white: #ffffff;
    --text-soft: #e6e6e6;
    --social: #3c86c6;
  }
  * { box-sizing: border-box; margin: 0; padding: 0; }
  html, body {
    width: 1200px; height: 800px; overflow: hidden;
    background: var(--bg);
    font-family: "Arimo", Arial, sans-serif;
  }
  .stage { position: relative; width: 1200px; height: 800px; }
  .card {
    position: absolute; top: 236px;
    width: 520px; height: 328px;
    background: var(--green);
    border-radius: 44px 8px 44px 44px;
    box-shadow: 0 10px 24px rgba(0,0,0,0.18);
    overflow: hidden;
  }
  .card--front { left: 60px; }
  .card--back { left: 620px; }
  .card__face {
    position: absolute; left: 0; top: 0; right: 0; bottom: 30px;
    background: var(--card);
    border-radius: 44px 8px 44px 44px;
  }
  .card__edge-url {
    position: absolute; left: 46px; bottom: 8px;
    font-size: 13px; color: var(--white); letter-spacing: 0.2px;
  }
  .brand {
    display: flex; flex-direction: column; align-items: flex-start; gap: 10px;
  }
  .brand__square {
    width: 44px; height: 44px; background: var(--green); border-radius: 5px;
  }
  .brand__name {
    font-weight: 700; color: var(--white); font-size: 24px; line-height: 1;
    white-space: nowrap;
  }
  .card--front .brand { position: absolute; left: 44px; top: 70px; }
  .holder { position: absolute; left: 300px; top: 112px; }
  .holder__name { font-weight: 700; color: var(--green); font-size: 22px; line-height: 1.15; }
  .holder__role { color: var(--text-soft); font-size: 21px; line-height: 1.15; }
  .contacts {
    position: absolute; left: 300px; top: 192px;
    list-style: none; color: var(--text-soft); font-size: 16px;
  }
  .contacts li { display: flex; align-items: center; gap: 7px; height: 23px; white-space: nowrap; }
  .icon {
    width: 16px; height: 16px; background: var(--green); border-radius: 3px;
    display: inline-flex; align-items: center; justify-content: center;
  }
  .contacts__social { gap: 10px !important; }
  .social { display: inline-flex; align-items: center; gap: 5px; }
  .social__square { width: 14px; height: 14px; background: var(--social); border-radius: 2px; }
  .card--back .brand {
    position: absolute; left: 0; right: 0; top: 74px; align-items: center;
  }
  .card__url {
    position: absolute; left: 0; right: 0; top: 182px; text-align: center;
    font-size: 13px; color: var(--text-soft);
  }
  .card__states {
    position: absolute; left: 0; right: 0; top: 206px; text-align: center;
    font-size: 13px; font-weight: 700; color: var(--green); letter-spacing: 1px;
  }
</style>
</head>
<body>
<main class="stage">
  <section class="card card--front" aria-label="Card front">
    <div class="card__face">
      <div class="brand">
        <span class="brand__square"></span>
        <span class="brand__name">KBMR Planning</span>
      </div>
      <div class="holder">
        <p class="holder__name">Harper</p>
        <p class="holder__role">Manager</p>
      </div>
      <ul class="contacts">
        <li>
          <span class="icon" aria-hidden="true">
            <svg width="10" height="10" viewBox="0 0 24 24"><path fill="#fff" d="M6.6 10.8a15 15 0 0 0 6.6 6.6l2.2-2.2c.3-.3.7-.4 1-.2 1.1.4 2.3.6 3.6.6.6 0 1 .4 1 1V20c0 .6-.4 1-1 1A17 17 0 0 1 3 4c0-.6.4-1 1-1h3.5c.6 0 1 .4 1 1 0 1.3.2 2.5.6 3.6.1.3 0 .7-.2 1z"/></svg>
          </span>1300 555 014
        </li>
        <li>
          <span class="icon" aria-hidden="true">
            <svg width="10" height="10" viewBox="0 0 24 24"><path fill="#fff" d="M2 5h20v14H2z"/><path fill="none" stroke="#5cc43a" stroke-width="2" d="M2 6l10 7 10-7"/></svg>
          </span>admin@kbmr.com.au
        </li>
        <li class="contacts__social">
          <span class="social"><span class="social__square"></span>kbmr</span>
          <span class="social"><span class="social__square"></span>kbmr</span>
          <span class="social"><span class="social__square"></span>kbmr</span>
        </li>
      </ul>
    </div>
    <p class="card__edge-url">www.kbmrplanning.com.au</p>
  </section>

  <section class="card card--back" aria-label="Card back">
    <div class="card__face">
      <div class="brand">
        <span class="brand__square"></span>
        <span class="brand__name">KBMR Planning</span>
      </div>
      <p class="card__url">www.kbmrplanning.com.au</p>
      <p class="card__states">VIC / NSW / QLD / TAS</p>
    </div>
  </section>
</main>
</body>
</html>
```